wealth management firm, professional group, new model

we have a logo that works but we need a card, white background using our colors...clean look

our tag line if can be used in

Steady Steps From Saver to Stakeholder

```html
<!DOCTYPE html>
<html lang="en">
<head>
<meta charset="utf-8">
<title>Calder Private Capital Group – Business Card</title>
<link rel="stylesheet" href="https://fonts.googleapis.com/css2?family=Open+Sans:wght@400;600;700&family=Roboto+Condensed:wght@400&display=swap">
<style>
  :root {
    --backdrop-top: #8aa6c6;
    --backdrop-bottom: #6f86ad;
    --navy: #1f3358;
    --navy-deep: #172a4c;
    --paper: #ffffff;
    --ink: #24385f;
    --ink-soft: #4a5d80;
    --on-navy: #ffffff;
    --on-navy-soft: #c9d3e4;
    --rule: rgba(255,255,255,0.55);
  }
  * { box-sizing: border-box; margin: 0; padding: 0; }
  html, body { width: 1200px; height: 876px; overflow: hidden; }
  body {
    position: relative;
    background: linear-gradient(160deg, var(--backdrop-top), var(--backdrop-bottom));
    font-family: "Open Sans", sans-serif;
  }
  .card {
    position: absolute;
    width: 520px;
    height: 297px;
    border-radius: 3px;
    box-shadow: 0 14px 30px rgba(20, 35, 70, 0.28);
  }

  .brand { text-align: center; }
  .brand__row {
    display: inline-flex;
    align-items: center;
    gap: 12px;
  }
  .brand__dot {
    width: 14px; height: 14px;
    border-radius: 50%;
    background: currentColor;
  }
  .brand__name {
    font-weight: 600;
    font-size: 40px;
    line-height: 1;
  }
  .brand__descriptor {
    display: block;
    font-weight: 400;
    font-size: 14px;
    margin-top: 8px;
  }

  /* Front: white */
  .card--front {
    left: 620px; top: 150px;
    background: var(--paper);
    color: var(--ink);
  }
  .card--front .brand { position: absolute; left: 0; right: 0; top: 84px; }
  .card--front .brand__descriptor { color: var(--ink-soft); }
  .tagline {
    position: absolute; left: 0; right: 0; bottom: 60px;
    text-align: center;
    font-size: 14px;
    font-style: normal;
    color: var(--ink);
  }

  /* Back: navy */
  .card--back {
    left: 80px; top: 440px;
    background: linear-gradient(135deg, var(--navy), var(--navy-deep));
    color: var(--on-navy);
  }
  .card--back .brand { position: absolute; left: 0; right: 0; top: 30px; }
  .card--back .brand__name { font-size: 28px; }
  .card--back .brand__dot { width: 10px; height: 10px; }
  .card--back .brand__descriptor { font-size: 11px; margin-top: 5px; color: var(--on-navy-soft); }
  .person { position: absolute; left: 0; right: 0; top: 116px; text-align: center; }
  .person__name { font-weight: 700; font-size: 17px; }
  .person__role { font-size: 12px; color: var(--on-navy-soft); margin-top: 1px; }

  .contacts {
    position: absolute; left: 24px; right: 24px; bottom: 24px;
    display: flex; align-items: flex-end;
  }
  .contact { flex: 1; display: flex; flex-direction: column; align-items: center; gap: 10px; }
  .contact__icon { width: 34px; height: 34px; }
  .contact__text {
    font-family: "Roboto Condensed", sans-serif;
    font-size: 13px;
    color: var(--on-navy-soft);
  }
  .contacts__rule { width: 1px; height: 36px; background: var(--rule); margin-bottom: 4px; }
</style>
</head>
<body>

  <section class="card card--front">
    <div class="brand">
      <div class="brand__row">
        <span class="brand__dot"></span>
        <span class="brand__name">Calder</span>
      </div>
      <span class="brand__descriptor">Private Capital Group</span>
    </div>
    <p class="tagline">Steady Steps From Saver to Stakeholder</p>
  </section>

  <section class="card card--back">
    <div class="brand">
      <div class="brand__row">
        <span class="brand__dot"></span>
        <span class="brand__name">Calder</span>
      </div>
      <span class="brand__descriptor">Private Capital Group</span>
    </div>
    <div class="person">
      <p class="person__name">Daniel Reyes</p>
      <p class="person__role">Director</p>
    </div>

    <div class="contacts">
      <div class="contact contact--web">
        <svg class="contact__icon" viewBox="0 0 34 34" aria-hidden="true">
          <circle cx="17" cy="17" r="16" fill="#fff"/>
          <circle cx="17" cy="17" r="9" fill="none" stroke="#1f3358" stroke-width="1.6"/>
          <ellipse cx="17" cy="17" rx="4" ry="9" fill="none" stroke="#1f3358" stroke-width="1.4"/>
          <line x1="8" y1="17" x2="26" y2="17" stroke="#1f3358" stroke-width="1.4"/>
        </svg>
        <span class="contact__text">caldercapital.com</span>
      </div>
      <span class="contacts__rule"></span>
      <div class="contact contact--phone">
        <svg class="contact__icon" viewBox="0 0 34 34" aria-hidden="true">
          <circle cx="17" cy="17" r="16" fill="#fff"/>
          <path d="M11 10.5c1-1 2.2-.8 2.8.2l1.4 2.4c.4.8.2 1.6-.5 2.1l-1 .7c.8 1.9 2.4 3.5 4.3 4.3l.7-1c.5-.7 1.3-.9 2.1-.5l2.4 1.4c1 .6 1.2 1.8.2 2.8l-1 1c-1.2 1.2-3.4 1.2-6.2-.6-2.4-1.6-4.6-3.8-6.2-6.2-1.8-2.8-1.8-5-.6-6.2z" fill="#1f3358"/>
        </svg>
        <span class="contact__text">020 555 0148</span>
      </div>
      <span class="contacts__rule"></span>
      <div class="contact contact--email">
        <svg class="contact__icon" viewBox="0 0 34 34" aria-hidden="true">
          <circle cx="17" cy="17" r="16" fill="#fff"/>
          <rect x="9" y="11.5" width="16" height="11" rx="1" fill="none" stroke="#1f3358" stroke-width="1.6"/>
          <path d="M9.5 12.5l7.5 6 7.5-6" fill="none" stroke="#1f3358" stroke-width="1.6"/>
        </svg>
        <span class="contact__text">hello@caldercapital.co</span>
      </div>
    </div>
  </section>

</body>
</html>
```